Brightfield Yard Service and Beyond LLC

• Mowing
• Weed eating
•Edging
• hedge trimming
• landscaping
•mulching
•yard clean up
• pressure washing

Target Market(s)

Everyone

Contact Information for Business Card

Licensed and insured

Font styles to use
Serif

Colors
59FF00
82FF00
B8FF75
E3FFCB
F4FFEA
F0912C
F2A743
F7CA91
FBE8D2
FDF5EE
EE7325
F08F49
F5BC92
FAE3D3
FDF4ED
EB3D1F
EC4F4E
F09395
F8D3D4
FCEDEE
E54698
E96AAD
F1A4CE
F9D9EA
FCEFF6

```html
<!DOCTYPE html>
<html lang="en">
<head>
<meta charset="utf-8">
<title>Brightfield Yard Service and Beyond LLC — Business Card</title>
<link href="https://fonts.googleapis.com/css2?family=Montserrat:wght@500;700;800&display=swap" rel="stylesheet">
<style>
  :root{
    --page:#eef0ea;
    --grass-dark:#0b3d0f;
    --grass-mid:#1a6b1c;
    --grass-light:#2f8f24;
    --brand-green:#1b7a1f;
    --white:#ffffff;
    --card-shadow:rgba(0,0,0,.18);
  }
  *{box-sizing:border-box;margin:0;padding:0}
  html,body{width:1200px;height:1200px;overflow:hidden;background:var(--page)}
  body{font-family:"Montserrat",sans-serif;position:relative}
  .card{
    position:absolute;left:150px;width:900px;height:514px;
    border-radius:34px;overflow:hidden;
    box-shadow:0 10px 30px var(--card-shadow);
  }
  .card--front{top:64px}
  .card--back{top:622px;background:var(--white)}

  .grass-photo{
    position:absolute;inset:0;
    background:radial-gradient(ellipse at 40% 40%,var(--grass-light) 0%,var(--grass-mid) 45%,var(--grass-dark) 100%);
  }

  /* front */
  .front-brand{position:absolute;left:70px;top:110px;width:380px;color:var(--white)}
  .brand-mark{width:70px;height:70px;border-radius:50%;background:currentColor;margin-bottom:22px}
  .brand-name{font-weight:800;font-size:34px;line-height:1.12;letter-spacing:.5px;text-transform:uppercase}
  .services{position:absolute;left:530px;top:110px;color:var(--white);font-weight:700;text-transform:uppercase}
  .services__title{font-size:25px;letter-spacing:6px;margin-bottom:10px}
  .services__list{list-style:none;font-size:18px;letter-spacing:3.5px;line-height:1.35}
  .services__list li::before{content:"•";margin-right:4px}
  .credential{
    position:absolute;left:0;right:0;bottom:44px;text-align:center;
    color:var(--white);font-weight:800;font-size:40px;letter-spacing:12px;text-transform:uppercase;
  }

  /* back */
  .person{position:absolute;left:60px;top:70px;color:var(--brand-green)}
  .person__name{font-weight:800;font-size:36px}
  .person__role{font-weight:500;font-size:24px;margin-top:2px}
  .contact{position:absolute;left:60px;bottom:60px;color:var(--brand-green)}
  .contact__phone{font-weight:800;font-size:52px;letter-spacing:1px;margin-bottom:8px}
  .contact__line{font-weight:700;font-size:17px;line-height:1.45}
  .back-brand{position:absolute;right:60px;top:110px;width:330px;color:var(--brand-green);text-align:left}
  .back-brand .brand-mark{width:64px;height:64px}
  .social{position:absolute;right:64px;bottom:58px;display:flex;align-items:center;gap:12px;color:var(--brand-green)}
  .social__label{font-weight:800;font-size:17px;letter-spacing:.5px;text-transform:uppercase;margin-right:4px}
  .social__dot{width:30px;height:30px;border-radius:50%;background:var(--brand-green)}
</style>
</head>
<body>

<section class="card card--front">
  <div class="grass-photo" role="img" aria-label="Close-up photograph of green lawn grass"></div>

  <div class="front-brand">
    <div class="brand-mark"></div>
    <div class="brand-name">Brightfield Yard Service and Beyond LLC</div>
  </div>

  <div class="services">
    <h2 class="services__title">Services Offered:</h2>
    <ul class="services__list">
      <li>Mowing</li>
      <li>Weed Eating</li>
      <li>Edging</li>
      <li>Hedge Trimming</li>
      <li>Landscaping</li>
      <li>Mulching</li>
      <li>Yard Clean Up</li>
      <li>Pressure Washing</li>
    </ul>
  </div>

  <p class="credential">Licensed and Insured</p>
</section>

<section class="card card--back">
  <div class="person">
    <h1 class="person__name">Dana Merrill, DVM</h1>
    <p class="person__role">Managing Director</p>
  </div>

  <div class="contact">
    <p class="contact__phone">(480) 555-0147</p>
    <p class="contact__line">hello@brightfieldyard.com &nbsp;-&nbsp; www.brightfieldyard.com</p>
    <p class="contact__line">2450 E. Willow Rd, Scottsdale, AZ 85250</p>
  </div>

  <div class="back-brand">
    <div class="brand-mark"></div>
    <div class="brand-name">Brightfield Yard Service and Beyond LLC</div>
  </div>

  <div class="social">
    <span class="social__label">Find us on:</span>
    <span class="social__dot" aria-hidden="true"></span>
    <span class="social__dot" aria-hidden="true"></span>
    <span class="social__dot" aria-hidden="true"></span>
  </div>
</section>

</body>
</html>
```